Forest Consultant/Timber Buyer needs a clean business card

We are a forestry consulting and timber buying company. We meet with private landowners and assist them with timber management and timber harvesting. We would like a professional business card, please no clip art. logo is blue and white but would like to see a gray,silver, or some other color incorporated. Would like basic contact info. Would like to the layout to be creative and sleek but masculine.

Target Market(s)

private landowners

Industry/Entity Type

Business

Contact Information for Business Card

name,position, cell number, office number, email, website. This might be to cluttered. Basic contact info is what we are looking for.

Contact info can all be on one side with logo on the other.

Font styles to use
Serif
Sans Serif

Colors
0255a3
ffffff
aaaaaa

Requirements
Must have
• We just want it professional.
Nice to have
• Creative layout.
Should not have
• please no clip art of log trucks etc.

```html
<!DOCTYPE html>
<html lang="en">
<head>
<meta charset="utf-8">
<title>Ridgeline Land &amp; Timber – Business Card</title>
<link href="https://fonts.googleapis.com/css2?family=Lato:wght@400;700;900&display=swap" rel="stylesheet">
<style>
  :root {
    --brand-blue: #0255a3;
    --card-white: #ffffff;
    --silver: #aaaaaa;
    --silver-light: #e4e4e4;
    --ink: #1a1a1a;
    --backdrop: #3a3a3c;
  }
  * { box-sizing: border-box; margin: 0; padding: 0; }
  html, body {
    width: 1200px; height: 900px; overflow: hidden;
    background: var(--backdrop);
    font-family: "Lato", Arial, sans-serif;
  }
  .sheet { position: relative; width: 1200px; height: 900px; }
  .card {
    position: absolute; left: 260px; width: 680px; height: 389px;
    overflow: hidden;
    box-shadow: 0 14px 30px rgba(0,0,0,.45);
  }
  .card--front { top: 50px; background: var(--brand-blue); }
  .card--back { top: 461px; background: var(--card-white); }
  .card__shape { position: absolute; inset: 0; }

  /* Wordmark: name in one colour and one weight, plain dot beside it */
  .wordmark {
    position: absolute; display: flex; align-items: center; gap: 14px;
    font-weight: 900; text-transform: uppercase; white-space: nowrap;
  }
  .wordmark__dot { border-radius: 50%; flex: none; }
  .wordmark__name { display: block; letter-spacing: .04em; line-height: 1; }
  .wordmark__sub { display: block; letter-spacing: .3em; line-height: 1; margin-top: 6px; }

  .card--front .wordmark {
    left: 0; right: 0; top: 120px; justify-content: center; color: var(--card-white);
  }
  .card--front .wordmark__dot { width: 34px; height: 34px; background: var(--card-white); }
  .card--front .wordmark__name { font-size: 46px; }
  .card--front .wordmark__sub { font-size: 17px; }

  .card--back .wordmark { left: 32px; top: 104px; color: var(--brand-blue); }
  .card--back .wordmark__dot { width: 22px; height: 22px; background: var(--brand-blue); }
  .card--back .wordmark { gap: 10px; }
  .card--back .wordmark__name { font-size: 28px; }
  .card--back .wordmark__sub { font-size: 11px; margin-top: 5px; }

  .front__web {
    position: absolute; left: 0; right: 0; top: 255px; text-align: center;
    color: var(--card-white); font-size: 18px; letter-spacing: .12em;
  }

  .contact-list {
    position: absolute; left: 40px; top: 178px; list-style: none;
    color: var(--ink); font-size: 18px; line-height: 26px;
  }
  .contact-list li { display: flex; align-items: center; gap: 12px; }
  .contact-list svg { width: 15px; height: 15px; flex: none; fill: var(--brand-blue); }

  .person { position: absolute; right: 40px; top: 150px; text-align: right; }
  .person__name { color: var(--card-white); font-size: 26px; font-weight: 400; letter-spacing: .02em; }
  .person__role { color: var(--silver-light); font-size: 19px; margin-top: 2px; }

  .address {
    position: absolute; right: 200px; bottom: 38px; text-align: right;
    color: var(--ink); font-size: 24px; line-height: 29px;
  }
</style>
</head>
<body>
<main class="sheet">

  <section class="card card--front" aria-label="Card front">
    <svg class="card__shape" viewBox="0 0 680 389" preserveAspectRatio="none" aria-hidden="true">
      <defs>
        <linearGradient id="silverBand" x1="0" x2="1" y1="0" y2="0">
          <stop offset="0" stop-color="#8f8f8f"/>
          <stop offset=".45" stop-color="#f2f2f2"/>
          <stop offset="1" stop-color="#9a9a9a"/>
        </linearGradient>
      </defs>
      <rect x="0" y="375" width="680" height="14" fill="url(#silverBand)"/>
    </svg>
    <div class="wordmark">
      <span class="wordmark__dot"></span>
      <span><span class="wordmark__name">Ridgeline</span><span class="wordmark__sub">Land &amp; Timber</span></span>
    </div>
    <p class="front__web">www.ridgelinetimber.com</p>
  </section>

  <section class="card card--back" aria-label="Card back">
    <svg class="card__shape" viewBox="0 0 680 389" preserveAspectRatio="none" aria-hidden="true">
      <defs>
        <linearGradient id="silverCurve" x1="0" x2="1" y1="0" y2="1">
          <stop offset="0" stop-color="#9c9c9c"/>
          <stop offset=".5" stop-color="#f4f4f4"/>
          <stop offset="1" stop-color="#8a8a8a"/>
        </linearGradient>
      </defs>
      <path d="M0,0 H680 V389 H548 C520,210 350,72 0,50 Z" fill="var(--brand-blue)"/>
      <path d="M0,50 C350,72 520,210 548,389" fill="none" stroke="url(#silverCurve)" stroke-width="9"/>
    </svg>

    <div class="wordmark">
      <span class="wordmark__dot"></span>
      <span><span class="wordmark__name">Ridgeline</span><span class="wordmark__sub">Land &amp; Timber</span></span>
    </div>

    <ul class="contact-list">
      <li><svg viewBox="0 0 16 16" aria-hidden="true"><path d="M3 1h3l1.5 4-2 1.3a9 9 0 0 0 4.2 4.2L11 8.5l4 1.5v3c0 1-1 2-2 2C6.5 15 1 9.5 1 3c0-1 1-2 2-2z"/></svg>512 555 0142</li>
      <li><svg viewBox="0 0 16 16" aria-hidden="true"><path d="M4 1h8v4H4zM1 6h14v6h-3v3H4v-3H1zm4 5v3h6v-3z"/></svg>512 555 0143</li>
      <li><svg viewBox="0 0 16 16" aria-hidden="true"><path d="M1 3h14v10H1zm1.5 1.2V5l5.5 4 5.5-4v-.8L8 8z"/></svg>info@ridgelinetimber.com</li>
      <li><svg viewBox="0 0 16 16" aria-hidden="true"><circle cx="8" cy="8" r="7"/></svg>www.ridgelinetimber.com</li>
    </ul>

    <div class="person">
      <p class="person__name">Marcus Hale</p>
      <p class="person__role">Manager</p>
    </div>

    <p class="address">4100 Pine Hollow Rd<br>Lufkin TX 75901</p>
  </section>

</main>
</body>
</html>
```